依頼詳細
販促の一環としてフリーペーパーに広告を出稿します。(A4・1ページ)
つきましてはA4広告1枚の制作をお願い致します。
【サイズ】 天地297mm × 左右210mm

■出稿にあたり意識すること

・ゴルフウェアのレンタルサービスがあるということを知ってもらうこと
・サービスの利便性を簡潔に訴えること(※◎の訴求は必須です。)
◎送料無料  ◎洗濯クリーニング不要  ◎1泊2日/¥2,100~
△添付の訴求バナー①内容(※できれば訴求したいです。)
・「初回無料キャンペーン」「フォトコンテスト」を実施中ということ

【添付】
・弊社ロゴ
・サービス訴求バナー
(送料無料)(洗濯・クリーニング不要)(1泊2日/¥2,100~)(訴求バナー①)
・参考例(2点)
・当方が制作したもの
記載項目
A4広告の制作にあたり添付バナーの使用は問いません。
(添付バナーの使用、ご自身で制作どちらも可です。)
サイズ
A4
ページ数
片面
希望イメージ
シンプル 複雑
単色 カラフル
暗い 明るい
日常 高級
遊び心 厳粛
未来的 伝統的
女性的 男性的
希望する色
納品ファイル
• 高解像度JPG (.jpg)
• イラストレーター形式 (.ai)
補足説明
■ 選んだ理由

ゴルフ+レンタル が良く伝わる素敵なデザインのため

■ 提案者全員のお礼・コメント

この度はご提案誠にありがとうございました。
今後もコンペ形式にてご依頼をしますので機会がございましたら宜しくお願い致します。

```html
<!DOCTYPE html>
<html lang="ja">
<head>
<meta charset="utf-8">
<title>ティーウェア ゴルフウェアのレンタルサービス</title>
<link href="https://fonts.googleapis.com/css2?family=M+PLUS+Rounded+1c:wght@500;700;800;900&family=Noto+Sans+JP:wght@500;700;900&display=swap" rel="stylesheet">
<style>
:root{
  --pink-bg:#f6c9cb;
  --pink-soft:#fbe1e1;
  --coral:#f06a5f;
  --red:#e8465a;
  --navy:#1f2b57;
  --green:#3aa34a;
  --white:#ffffff;
  --text:#333333;
}
*{margin:0;padding:0;box-sizing:border-box}
html,body{width:846px;height:1200px;overflow:hidden;background:var(--white)}
body{font-family:"M PLUS Rounded 1c","Noto Sans JP",sans-serif;color:var(--text)}
.ad{position:relative;width:846px;height:1200px;overflow:hidden;background:var(--pink-bg)}
.hero-photo{position:absolute;right:0;top:0;width:470px;height:835px;
  background:linear-gradient(160deg,#f9e3df 0%,#f3c4c4 55%,#eeb4b8 100%)}
.tagline{position:absolute;left:30px;top:60px;background:var(--white);color:var(--red);
  font-weight:800;font-size:24px;padding:6px 22px;border-radius:6px;letter-spacing:1px}
.title{position:absolute;left:40px;top:122px;font-family:"Noto Sans JP",sans-serif;font-weight:900;
  color:var(--navy);font-size:58px;line-height:78px;letter-spacing:2px;white-space:nowrap}
.brand{position:absolute;left:50px;top:300px;color:var(--navy);font-weight:900;
  font-size:128px;line-height:130px;letter-spacing:2px}
.brand-sub{position:absolute;left:130px;top:572px;color:var(--navy);font-weight:800;font-size:30px}
.badge{position:absolute;border-radius:50%;display:flex;flex-direction:column;align-items:center;
  justify-content:center;text-align:center;font-weight:900;white-space:nowrap}
.badge-campaign{left:545px;top:205px;width:150px;height:150px;background:var(--red);color:var(--white);
  font-size:21px;line-height:28px;border:4px solid var(--white)}
.badge-campaign .lead{font-size:18px}
.badge-contest{left:692px;top:318px;width:126px;height:126px;background:var(--white);color:var(--red);
  font-size:15px;line-height:24px}
.worries{position:absolute;left:40px;top:608px;width:766px;display:flex;justify-content:space-between}
.worry{width:226px;display:flex;flex-direction:column;align-items:center}
.bubble{position:relative;background:var(--white);border:3px solid var(--coral);border-radius:50%;
  width:220px;height:130px;display:flex;align-items:center;justify-content:center;text-align:center;
  font-weight:700;font-size:18px;line-height:25px;color:var(--text);padding:0 26px}
.bubble::after{content:"";position:absolute;bottom:-14px;left:50%;width:18px;height:18px;margin-left:-9px;
  background:var(--white);border-right:3px solid var(--coral);border-bottom:3px solid var(--coral);transform:rotate(45deg)}
.worry-figure{margin-top:18px;width:70px;height:70px;border-radius:50%;background:#fbdada}
.solve-band{position:absolute;left:0;top:838px;width:846px;height:54px;background:var(--coral);
  color:var(--white);font-weight:900;font-size:28px;display:flex;align-items:center;justify-content:center;letter-spacing:2px}
.points-area{position:absolute;left:0;top:892px;width:846px;height:178px;background:var(--pink-soft)}
.points{position:absolute;left:40px;top:910px;width:766px;display:flex;justify-content:space-between}
.point{width:240px;height:148px;background:var(--white);border:3px solid var(--coral);border-radius:8px;
  position:relative;text-align:center;padding-top:40px}
.point-label{position:absolute;left:50%;top:-16px;transform:translateX(-50%);background:var(--coral);color:var(--white);
  font-weight:900;font-size:16px;padding:4px 14px;border-radius:14px;white-space:nowrap}
.point-label b{font-size:22px}
.point-sub{font-weight:800;font-size:20px;color:var(--text)}
.point-main{font-weight:900;font-size:38px;color:var(--red);line-height:52px}
.point-main small{font-size:24px}
.flow{position:absolute;left:0;top:1070px;width:846px;height:130px;background:var(--white)}
.flow-heading{position:absolute;left:16px;top:8px;height:116px;writing-mode:vertical-rl;font-weight:900;font-size:17px;
  line-height:20px;color:var(--green);letter-spacing:1px;white-space:nowrap}
.steps{position:absolute;left:60px;top:10px;width:770px;display:flex;justify-content:space-between}
.step{width:120px;text-align:center}
.step-no{display:inline-block;background:var(--green);color:var(--white);font-weight:800;font-size:12px;
  padding:1px 8px;border-radius:8px}
.step-icon{width:60px;height:52px;margin:6px auto 4px;border-radius:8px;background:#f6e3b0}
.step-text{font-size:12px;font-weight:700;line-height:15px;color:var(--text)}
.step-arrow{position:absolute;left:0;top:38px}
</style>
</head>
<body>
<div class="ad">
  <div class="hero-photo" role="img" aria-label="白いキャップとピンクのゴルフウェアを着た女性のポートレート写真"></div>

  <p class="tagline">お手軽価格で最新のゴルフウェアが着れる！</p>
  <h1 class="title">ゴルフウェアの<br>レンタルサービス</h1>

  <div class="brand">TEE<br>wear</div>
  <p class="brand-sub">- ティーウェア -</p>

  <div class="badge badge-campaign"><span class="lead">今なら！</span><span>初回無料</span><span>キャンペーン</span></div>
  <div class="badge badge-contest"><span>フォトコンテスト</span><span>実施中！</span></div>

  <div class="worries">
    <div class="worry">
      <p class="bubble">ゴルフウェアは<br>高いから何着も<br>買えない…</p>
      <div class="worry-figure" role="img" aria-label="悩む女性の線画イラスト"></div>
    </div>
    <div class="worry">
      <p class="bubble">ファンデの汚れや<br>お手入れが<br>面倒…</p>
      <div class="worry-figure" role="img" aria-label="悩む女性の線画イラスト"></div>
    </div>
    <div class="worry">
      <p class="bubble">いつも同じ服を<br>着てラウンドを<br>するのは…</p>
      <div class="worry-figure" role="img" aria-label="悩む女性の線画イラスト"></div>
    </div>
  </div>

  <div class="solve-band">ティーウェアならこんなお悩みすべて解決！</div>

  <div class="points-area"></div>
  <div class="points">
    <div class="point">
      <span class="point-label">point <b>1</b></span>
      <p class="point-sub">1泊2日</p>
      <p class="point-main">¥2,100<small>〜</small></p>
    </div>
    <div class="point">
      <span class="point-label">point <b>2</b></span>
      <p class="point-sub">洗濯・クリーニング</p>
      <p class="point-main">不要！</p>
    </div>
    <div class="point">
      <span class="point-label">point <b>3</b></span>
      <p class="point-sub">お手軽に試せる！</p>
      <p class="point-main">送料無料</p>
    </div>
  </div>

  <section class="flow">
    <h2 class="flow-heading">ご利用の流れ</h2>
    <div class="steps">
      <div class="step"><span class="step-no">step01</span><div class="step-icon" role="img" aria-label="黄色いポロシャツのイラスト"></div><p class="step-text">商品を選択</p></div>
      <div class="step"><span class="step-no">step02</span><div class="step-icon" role="img" aria-label="カレンダーのイラスト"></div><p class="step-text">プレー日を選択</p></div>
      <div class="step"><span class="step-no">step03</span><div class="step-icon" role="img" aria-label="配送トラックのイラスト"></div><p class="step-text">プレー日前日に<br>商品を受け取り</p></div>
      <div class="step"><span class="step-no">step04</span><div class="step-icon" role="img" aria-label="ゴルフをする人のイラスト"></div><p class="step-text">商品を着用し<br>ゴルフを楽しむ</p></div>
      <div class="step"><span class="step-no">step05</span><div class="step-icon" role="img" aria-label="段ボール箱のイラスト"></div><p class="step-text">プレー後、<br>その日のうちに返送</p></div>
    </div>
    <svg class="step-arrow" width="846" height="20" viewBox="0 0 846 20" aria-hidden="true">
      <g fill="var(--green)">
        <polygon points="210,4 220,10 210,16"/>
        <polygon points="372,4 382,10 372,16"/>
        <polygon points="534,4 544,10 534,16"/>
        <polygon points="696,4 706,10 696,16"/>
      </g>
    </svg>
  </section>
</div>
</body>
</html>
```